We need visit card and a letter paper for our website. thx

We have a beauty clinic in Switzerland.
https://wolkenbachtal.ch
We need a visit card.

Requirements
Must have
• see colors on website

```html
<!DOCTYPE html>
<html lang="en">
<head>
<meta charset="utf-8">
<title>Wolkenbachtal Beauty Clinic – Business Card</title>
<link rel="stylesheet" href="https://fonts.googleapis.com/css2?family=League+Spartan:wght@600;700&family=Poppins:wght@400;700&family=Marcellus&display=swap">
<style>
  :root {
    --page: #fbfbc5;
    --magenta: #dd2aac;
    --blush: #f9c9ec;
    --mist: #ececec;
    --slate: #7f8b8a;
    --ink: #111111;
    --white: #ffffff;
    --skin-light: #f6e6de;
    --skin: #e9c2ab;
    --tan: #c98e6c;
  }
  * { box-sizing: border-box; margin: 0; padding: 0; }
  html, body { width: 720px; height: 1200px; overflow: hidden; }
  body {
    background: var(--page);
    font-family: "Poppins", Arial, sans-serif;
    color: var(--ink);
    position: relative;
  }
  .side-label {
    position: absolute; left: 0; width: 720px; text-align: center;
    font-family: "Poppins", Arial, sans-serif; font-weight: 700; font-size: 40px;
    line-height: 1;
  }
  .side-label--front { top: 50px; }
  .side-label--back { top: 616px; }

  .card {
    position: absolute; left: 22px; width: 680px; height: 407px;
    background: var(--white); overflow: hidden;
  }
  .card--front { top: 147px; }
  .card--back { top: 689px; }

  .band { position: absolute; left: 0; width: 100%; }
  .band--magenta { top: 0; height: 42px; background: var(--magenta); }

  /* front */
  .doctor { position: absolute; top: 48px; }
  .doctor--left { left: 48px; }
  .doctor--right { right: 53px; text-align: right; }
  .doctor__name {
    font-family: "League Spartan", Arial, sans-serif; font-weight: 700;
    font-size: 25px; font-variant: small-caps; letter-spacing: 0.3px; line-height: 1;
  }
  .doctor__role { margin-top: 20px; font-size: 16px; line-height: 1; }

  .brand {
    position: absolute; left: 0; width: 100%; text-align: center;
    font-family: "Marcellus", Georgia, serif; font-size: 36px; line-height: 1;
  }
  .card--front .brand { top: 158px; }
  .card--back .brand { top: 132px; font-size: 40px; }

  .band--mist { top: 234px; height: 11px; background: var(--mist); }
  .band--blush-front { top: 245px; bottom: 0; background: var(--blush); }

  .portrait {
    position: absolute; left: 26px; top: 234px; width: 147px; height: 173px;
    background: linear-gradient(180deg, var(--skin-light) 0%, var(--skin) 60%, var(--skin-light) 100%);
  }

  .contact { position: absolute; right: 40px; top: 254px; list-style: none; }
  .contact__item {
    display: flex; justify-content: flex-end; align-items: center;
    height: 29px; font-size: 15px;
  }
  .contact__icon { width: 18px; height: 18px; margin-left: 17px; }

  /* back */
  .band--slate { top: 42px; height: 14px; background: var(--slate); }
  .band--blush-back { top: 246px; bottom: 0; background: var(--blush); }
  .figure-photo {
    position: absolute; left: 0; right: 0; top: 246px; bottom: 0;
    background: linear-gradient(180deg, var(--blush) 0%, var(--skin) 45%, var(--tan) 100%);
  }
</style>
</head>
<body>
  <h2 class="side-label side-label--front">Front</h2>
  <section class="card card--front">
    <div class="band band--magenta"></div>
    <div class="doctor doctor--left">
      <p class="doctor__name">Dr. Lena Marbach</p>
      <p class="doctor__role">FA for plastic surgery</p>
    </div>
    <div class="doctor doctor--right">
      <p class="doctor__name">Dr. Felix Ansorg</p>
      <p class="doctor__role">FA for anesthetist,DESA</p>
    </div>
    <p class="brand">Wolkenbachtal</p>
    <div class="band band--mist"></div>
    <div class="band band--blush-front"></div>
    <div class="portrait" role="img" aria-label="Photo of a smiling woman touching her face"></div>
    <ul class="contact">
      <li class="contact__item">+41 (0) 800 22 30 40
        <svg class="contact__icon" viewBox="0 0 20 20"><path d="M2 7c0-3 3-4 8-4s8 1 8 4v1h-4V6H6v2H2zM4 9h12l2 8H2z" fill="var(--ink)"/><circle cx="10" cy="13" r="2" fill="var(--white)"/></svg>
      </li>
      <li class="contact__item">https://wolkenbachtal.ch
        <svg class="contact__icon" viewBox="0 0 20 20" fill="none" stroke="var(--ink)" stroke-width="1.5"><circle cx="10" cy="10" r="8"/><ellipse cx="10" cy="10" rx="3.5" ry="8"/><path d="M2 10h16M3.5 6h13M3.5 14h13"/></svg>
      </li>
      <li class="contact__item">hallo@wolkenbachtal.ch
        <svg class="contact__icon" viewBox="0 0 20 20"><rect x="1" y="4" width="18" height="12" fill="var(--ink)"/><path d="M2 5l8 6 8-6" fill="none" stroke="var(--white)" stroke-width="1.4"/></svg>
      </li>
      <li class="contact__item">Talweg 4, 7000 Chur, Switzerland
        <svg class="contact__icon" viewBox="0 0 20 20"><path d="M10 1a6 6 0 0 1 6 6c0 4-6 12-6 12S4 11 4 7a6 6 0 0 1 6-6z" fill="var(--ink)"/><circle cx="10" cy="7" r="2.2" fill="var(--white)"/></svg>
      </li>
    </ul>
  </section>

  <h2 class="side-label side-label--back">Back</h2>
  <section class="card card--back">
    <div class="band band--magenta"></div>
    <div class="band band--slate"></div>
    <p class="brand">Wolkenbachtal</p>
    <div class="band band--blush-back"></div>
    <div class="figure-photo" role="img" aria-label="Photo of a tanned woman in a black bikini lying back"></div>
  </section>
</body>
</html>
```